Flyer für Hausärzte
Aufgabenstellung
Der Flyer soll das Format DIN 105 lang haben und später bei druckfalter.de gedruckt werden. Entsprechende Vorlagen sind bei druckfalter.de vorhanden. Der Flyer wird in der Mitte 1x gefalzt und beidseitige bedruckt. (Es gibt also eine Außenseite, eine Doppel Innenseiten und eine Rückseite)
Der Flyer soll Neupatienten sowie BEstandspatienten ansprechen und über die Ärzte und die Leistungen informieren. Siehe www.praxis-lindenbogen.de
Die Fotos auf der Homepage können verwendet werden, entsprechende Lizenzen für die Nutzung liegen vor. An besseren Ideen bin ich natürlich auch interessiert :-)
Datenübergabe in Adobe Illustrator (.ai) oder Adobe InDesign (.indd)
Vielen Dank und beste Grüße

```html
<!DOCTYPE html>
<html lang="de">
<head>
<meta charset="utf-8">
<title>Flyer Praxis Lindenbogen</title>
<link href="https://fonts.googleapis.com/css2?family=Outfit:wght@300;400;500;600&display=swap" rel="stylesheet">
<style>
:root{
  --bg:#ebebeb;
  --pink:#e4528f;
  --pink-deep:#d93d7f;
  --pink-soft:#f3a9c9;
  --pink-pale:#fbe3ee;
  --ink:#1c1c1c;
  --white:#ffffff;
  --photo-grey:#4a4a4a;
}
*{box-sizing:border-box;margin:0;padding:0}
html,body{width:1200px;height:1174px;overflow:hidden;background:var(--bg);font-family:"Outfit",sans-serif;color:var(--ink)}
.canvas{position:relative;width:1200px;height:1174px}
.spread{position:absolute;top:294px;width:585px;height:585px;display:flex}
.spread--outside{left:10px}
.spread--inside{left:605px}
.panel{position:relative;width:292.5px;height:585px;overflow:hidden}
.panel--back{background:linear-gradient(180deg,var(--pink-soft) 0%,var(--pink-pale) 45%,var(--white) 100%);text-align:center}
.panel--front{background:linear-gradient(180deg,var(--pink-soft) 0%,var(--white) 30%);border-left:1px solid #f1c3d7}
.panel--team{background:linear-gradient(180deg,var(--pink-soft) 0%,var(--pink-pale) 50%,var(--pink-soft) 100%)}
.panel--services{background:linear-gradient(180deg,var(--pink-soft) 0%,var(--pink-pale) 50%,var(--pink-soft) 100%);border-left:1px solid var(--pink-soft)}

.contact{position:absolute;top:26px;left:0;right:0;font-size:11.5px;line-height:1.35}
.contact h2{font-size:15px;font-weight:500;margin-bottom:2px}
.contact b{font-weight:600}
.rule{position:absolute;left:42px;right:42px;height:2px;background:var(--pink)}
.cta{position:absolute;top:152px;left:0;right:0;color:var(--pink);font-size:16.5px;line-height:1.05;font-weight:400;letter-spacing:.3px}
.hours{position:absolute;top:268px;left:0;right:0}
.hours h2{font-size:19.5px;font-weight:500;margin-bottom:10px}
.hours table{margin-left:55px;border-collapse:collapse;font-size:12px;text-align:left}
.hours td{vertical-align:top;padding-bottom:8px;line-height:1.1}
.hours td.day{width:104px;font-weight:500;letter-spacing:.6px}
.hours td.time{color:var(--pink)}
.note{position:absolute;top:470px;left:0;right:0;font-size:10.5px;font-weight:300}
.location{position:absolute;top:520px;left:0;right:0}
.location h3{font-size:14.5px;font-weight:500}
.location p{font-size:11.5px;font-weight:300;margin-top:4px}

.brand{position:absolute;top:28px;left:24px;display:flex;align-items:center;gap:8px}
.brand__mark{width:16px;height:16px;border:3px solid var(--ink)}
.brand__name{font-size:21px;font-weight:500;color:var(--pink);letter-spacing:.5px}
.claim{position:absolute;top:96px;left:0;right:0;text-align:center;font-size:14px;line-height:1.3}
.hero{position:absolute;top:138px;left:0;width:292.5px;height:336px;background:linear-gradient(160deg,#d8d2cb 0%,#a79d93 45%,#e9e6e2 100%)}
.slogan{position:absolute;top:484px;left:0;right:0;text-align:center;font-size:17.5px;line-height:1.4}

.team-head{position:absolute;top:14px;left:0;right:0;text-align:center}
.team-head h2{font-size:15px;font-weight:500}
.team-head p{font-size:9px;font-weight:500;line-height:1.25;margin-top:2px}
.member{position:absolute;left:17px;display:flex;align-items:center;gap:18px}
.member__photo{width:84px;height:84px;border-radius:50%;border:3px solid var(--white);background:radial-gradient(circle at 50% 40%,#8a8580 0%,var(--photo-grey) 70%);flex:none}
.member__name{color:var(--pink);font-size:12px;margin-bottom:10px}
.member__role{font-size:9px;font-weight:500;line-height:1.15}

.service{position:absolute;display:flex;align-items:center;gap:10px}
.service--left{left:13px}
.service--right{right:13px;text-align:right}
.service__photo{width:79px;height:79px;border-radius:50%;border:2.5px solid var(--pink-deep);flex:none}
.service__label{font-size:12px;font-weight:500;line-height:1.05}
</style>
</head>
<body>
<div class="canvas">

  <section class="spread spread--outside">
    <div class="panel panel--back">
      <div class="contact">
        <h2>Unsere Kontaktdaten</h2>
        <p><b>Telefon:</b> 06221-48230</p>
        <p><b>Telefax:</b> 06221-482399</p>
        <p><b>E-Mail:</b> praxis@praxis-lindenbogen.de</p>
      </div>
      <div class="rule" style="top:127px"></div>
      <p class="cta">Kümmere dich heute noch<br>um dich selbst<br>– vereinbare einfach<br>einen Termin!</p>
      <div class="rule" style="top:240px"></div>
      <div class="hours">
        <h2>Sprechzeiten der Praxis</h2>
        <table>
          <tr><td class="day">Mo – Di</td><td class="time">08:30 – 12:00<br>15:00 – 18:00</td></tr>
          <tr><td class="day">Mittwoch</td><td class="time">08:30 – 12:00</td></tr>
          <tr><td class="day">Donnerstag</td><td class="time">08:30 – 12:00<br>15:00 – 18:00</td></tr>
          <tr><td class="day">Freitag</td><td class="time">08:30 – 12:00</td></tr>
          <tr><td class="day">Sa – So</td><td class="time">Geschlossen</td></tr>
        </table>
      </div>
      <p class="note">Termine nach Vereinbarung</p>
      <div class="rule" style="top:503px"></div>
      <div class="location">
        <h3>Standort unserer Hausarztpraxis</h3>
        <p>Ahornstraße 24, 67059 Lindenfeld</p>
      </div>
    </div>

    <div class="panel panel--front">
      <div class="brand">
        <span class="brand__mark"></span>
        <span class="brand__name">Praxis Lindenbogen</span>
      </div>
      <p class="claim">Ihre Hausarztpraxis im<br>Lindenbogen-Viertel</p>
      <div class="hero" role="img" aria-label="Foto: drei Generationen, Großmutter, Mutter und Tochter, lächelnd auf einem Sofa"></div>
      <p class="slogan">Gesundheit ein Leben lang –<br>wir gehen jeden<br>Schritt mit Ihnen</p>
    </div>
  </section>

  <section class="spread spread--inside">
    <div class="panel panel--team">
      <div class="team-head">
        <h2>Unser Team</h2>
        <p>Lernen Sie uns kennen – unser Team vereint Kompetenz,<br>Herz und Engagement. Lasst uns bekannt werden!</p>
      </div>
      <div class="member" style="top:66px">
        <div class="member__photo" role="img" aria-label="Porträtfoto Dr. Katrin Albers"></div>
        <div><p class="member__name">Dr. Katrin Albers</p><p class="member__role">Fachärztin für Allgemeinmedizin</p></div>
      </div>
      <div class="member" style="top:170px">
        <div class="member__photo" role="img" aria-label="Porträtfoto Dr. Laura Venzke"></div>
        <div><p class="member__name">Dr. Laura Venzke</p><p class="member__role">Fachärztin für Allgemeinmedizin</p></div>
      </div>
      <div class="member" style="top:269px">
        <div class="member__photo" role="img" aria-label="Porträtfoto Petra Lohmann"></div>
        <div><p class="member__name">Petra Lohmann</p><p class="member__role">Medizinische Fachangestellte (MFA)</p></div>
      </div>
      <div class="member" style="top:377px">
        <div class="member__photo" role="img" aria-label="Porträtfoto Julia Brenner"></div>
        <div><p class="member__name">Julia Brenner</p><p class="member__role">Medizinische Fachangestellte (MFA),<br>Versorgungsassistentin<br>in der Hausarztpraxis (VERAH)</p></div>
      </div>
      <div class="member" style="top:482px">
        <div class="member__photo" role="img" aria-label="Porträtfoto Andrea Seidel"></div>
        <div><p class="member__name">Andrea Seidel</p><p class="member__role">Medizinische Fachangestellte (MFA)</p></div>
      </div>
    </div>

    <div class="panel panel--services">
      <div class="service service--left" style="top:17px">
        <div class="service__photo" role="img" aria-label="Foto: Blutprobenröhrchen" style="background:linear-gradient(135deg,#f7dbe7,#e9c4d6)"></div>
        <p class="service__label">Diagnostische Möglichkeiten<br>und Gesundheitsvorsorge</p>
      </div>
      <div class="service service--right" style="top:82px">
        <p class="service__label">Checkup und Checkup Plus</p>
        <div class="service__photo" role="img" aria-label="Foto: Stethoskop" style="background:linear-gradient(135deg,#dfe6ee,#e58ab0)"></div>
      </div>
      <div class="service service--left" style="top:149px">
        <div class="service__photo" role="img" aria-label="Illustration: Darm" style="background:linear-gradient(135deg,#fbe8ef,#f1b9cd)"></div>
        <p class="service__label">Darmkrebsvorsorge</p>
      </div>
      <div class="service service--right" style="top:212px">
        <p class="service__label">Hautkrebsscreening</p>
        <div class="service__photo" role="img" aria-label="Foto: Dermatoskop an der Haut" style="background:linear-gradient(135deg,#d7c0c4,#f0a8c6)"></div>
      </div>
      <div class="service service--left" style="top:280px">
        <div class="service__photo" role="img" aria-label="Foto: Ultraschalluntersuchung" style="background:linear-gradient(135deg,#9fa8b3,#d9dde2)"></div>
        <p class="service__label">Screening auf<br>Bauchaortenaneurysma</p>
      </div>
      <div class="service service--right" style="top:349px">
        <p class="service__label" style="text-align:left">DMP<br>(Disease Managment<br>Program)</p>
        <div class="service__photo" role="img" aria-label="Foto: Blutzuckermessung" style="background:linear-gradient(135deg,#e8e4e2,#a89d98)"></div>
      </div>
      <div class="service service--left" style="top:422px">
        <div class="service__photo" role="img" aria-label="Foto: Hände halten ein Herz mit Familie" style="background:linear-gradient(135deg,#eeeeee,#ee7fae)"></div>
        <p class="service__label">Hausarztzentrierte<br>Versorgung (HZV)</p>
      </div>
      <div class="service service--right" style="top:488px">
        <p class="service__label">Impfberatung/Reisemedizin</p>
        <div class="service__photo" role="img" aria-label="Foto: Impfspritze" style="background:linear-gradient(135deg,#c9cdd2,#8fd0df)"></div>
      </div>
    </div>
  </section>

</div>
</body>
</html>
```